Leaflet aimed at owners of parking spaces and how they could be making money

We are developing a parking website which is a notice board for car space owners (which must be companies or organisations based in London)to advertise and rent these spaces to motorists
We need a double sided A5 leaflet aimed at owners -DOUBLE SIDED-the same colours as homepage attached (dark blue/light blue/white
To incorporate the 2 visuals man & money woman & p sign from home page
Keeping it simple would be okay
Text attached
use slotnimbly from the home page (same colours and style) and should read slotnimbly.com on the leaflet
Updates

Target Market(s)

this leaflet is aimed at owners of parking spaces-we want the owners to advertise their spaces on our website

Industry/Entity Type

Parking

Font styles to use
Serif
Sans Serif

Requirements
Must have
• same colours as home page
• 2 visuals
• woman and p sign
• man/car/pound coins
• slotnimbly.com instead of slotnimbly as on home page keep the same style and colours
Nice to have
• the visual of the man/car/money should be more prominent/larger than woman with P sign
• as the leaflet is telling owners of parking spaces they can make money from the parking spaces
Should not have
• this leaflet should NOT be aimed at motorists needing to book a parking space

```html
<!DOCTYPE html>
<html lang="en">
<head>
<meta charset="utf-8">
<title>slotnimbly.com – Owner Leaflet</title>
<link rel="stylesheet" href="https://fonts.googleapis.com/css2?family=Exo+2:wght@300;400;600&display=swap">
<style>
  :root {
    --ink-blue: #0b4f8f;
    --deep-blue: #1f4aa0;
    --panel-blue: #1579c4;
    --sky-cyan: #2ec0ee;
    --brand-blue: #1a7fc6;
    --white: #ffffff;
    --photo-blue: #2d6bbd;
    --photo-pale: #e9eef4;
  }
  * { margin: 0; padding: 0; box-sizing: border-box; }
  html, body { width: 1200px; height: 1000px; overflow: hidden; background: var(--white); }
  body { position: relative; font-family: "Exo 2", sans-serif; }

  .leaflet { position: absolute; left: 15px; top: 88px; width: 1170px; height: 824px; }

  .header-band {
    position: absolute; left: 0; top: 0; width: 100%; height: 62px;
    background: linear-gradient(90deg, #2a4ea8 0%, #7fb4de 35%, #d6e8f6 62%, #ffffff 85%);
  }
  .brand-name {
    position: absolute; right: 52px; top: 18px;
    font-weight: 400; font-size: 27px; letter-spacing: 0.5px; color: var(--brand-blue);
  }
  .header-rule { position: absolute; left: 0; top: 60px; width: 100%; height: 7px; background: var(--sky-cyan); }

  .main-panel {
    position: absolute; left: 0; top: 67px; width: 100%; height: 757px;
    background: radial-gradient(ellipse at 40% 40%, #1a86d0 0%, var(--panel-blue) 50%, #1560b0 100%);
    overflow: hidden;
  }

  .hero-photo { position: absolute; left: 0; top: 0; width: 560px; height: 425px; }

  .intro-box {
    position: absolute; left: 0; top: 455px; width: 548px; height: 150px;
    background: var(--white); border: 8px solid var(--sky-cyan); border-left: none;
    border-radius: 0 22px 22px 0;
    display: flex; align-items: center; justify-content: center; text-align: center;
    color: var(--ink-blue); font-size: 20.5px; line-height: 29px; padding: 0 16px;
  }
  .free-note {
    position: absolute; left: 30px; top: 640px; width: 500px; text-align: center;
    color: var(--white); font-size: 20.5px; line-height: 29px;
  }

  .steps-frame {
    position: absolute; left: 596px; top: 18px; width: 543px; height: 664px;
    border: 3px solid var(--white); border-radius: 26px;
  }
  .steps-title {
    position: absolute; left: 0; top: 14px; width: 100%; text-align: center;
    color: var(--white); font-weight: 600; font-size: 34px; letter-spacing: 1.5px;
  }
  .step {
    position: absolute; left: 27px; width: 484px;
    border: 2px solid var(--white); border-radius: 20px;
  }
  .step-one { top: 57px; height: 172px; }
  .step-two { top: 244px; height: 186px; }
  .step-three { top: 451px; height: 186px; }

  .step-badge {
    position: absolute; left: 21px; width: 113px;
    border: 1.5px solid var(--white); border-top: none;
    color: var(--white); font-size: 17.5px; line-height: 24px; text-align: center;
    text-transform: uppercase;
  }
  .step-badge::before {
    content: ""; position: absolute; left: -1.5px; right: -1.5px; top: 0;
    border-top: 1.5px solid var(--white);
  }
  .step-one .step-badge { top: 12px; height: 125px; padding-top: 12px; }
  .step-two .step-badge { top: 25px; height: 130px; padding-top: 12px; }
  .step-three .step-badge { top: 16px; height: 127px; padding-top: 10px; }
  .step-icon { position: absolute; left: 50%; transform: translateX(-50%); }

  .step-text {
    position: absolute; right: 6px; color: var(--white);
    font-weight: 300; font-size: 14.5px; line-height: 21px; letter-spacing: 0.6px;
    text-align: center; text-transform: uppercase;
  }
  .step-one .step-text { left: 150px; top: 34px; }
  .step-two .step-text { left: 140px; top: 6px; right: 2px; }
  .step-three .step-text { left: 150px; top: 36px; }

  .eligibility-note {
    position: absolute; left: 606px; top: 692px; color: var(--white);
    font-size: 15.5px; letter-spacing: 0.2px;
  }
</style>
</head>
<body>
  <div class="leaflet">
    <header class="header-band">
      <span class="brand-name">SLOTNIMBLY.COM</span>
    </header>
    <div class="header-rule"></div>

    <main class="main-panel">
      <svg class="hero-photo" viewBox="0 0 560 425" role="img" aria-label="Smiling businesswoman in glasses holding a blue parking P sign">
        <defs>
          <radialGradient id="photoTone" cx="0.45" cy="0.45" r="0.7">
            <stop offset="0" stop-color="#f4f6f9"/>
            <stop offset="0.55" stop-color="#c9d8ea"/>
            <stop offset="1" stop-color="#5d8fcc"/>
          </radialGradient>
        </defs>
        <circle cx="250" cy="120" r="300" fill="url(#photoTone)" stroke="#2ec0ee" stroke-width="9"/>
      </svg>

      <div class="intro-box">
        <p>You can now join many other businesses &amp; organisations such as churches, hotels and supermarkets that have realised parking spaces not in constant use can make an income.</p>
      </div>

      <p class="free-note">The website is FREE to use, so you'll never have to pay us a penny and your advert can be paused, altered or deleted at any time.</p>

      <section class="steps-frame">
        <h2 class="steps-title">HOW IT WORKS</h2>

        <div class="step step-one">
          <div class="step-badge">Post your<br>space<br>listing
            <svg class="step-icon" style="top:96px" width="50" height="40" viewBox="0 0 50 40">
              <g fill="#fff" transform="rotate(40 25 20)">
                <rect x="17" y="0" width="16" height="5" rx="1"/>
                <rect x="20" y="5" width="10" height="12"/>
                <path d="M12 17 H38 L35 22 H15 Z"/>
                <rect x="24" y="22" width="2" height="16"/>
              </g>
            </svg>
          </div>
          <p class="step-text">You complete an advert online, setting the price per day along with the days &amp; times when your parking space(s) are available.</p>
        </div>

        <div class="step step-two">
          <div class="step-badge">Renter<br>reserves<br>your space
            <svg class="step-icon" style="top:90px" width="52" height="52" viewBox="0 0 52 52">
              <rect x="2" y="2" width="48" height="48" fill="none" stroke="#fff" stroke-width="3"/>
              <rect x="8" y="8" width="36" height="36" fill="#fff"/>
              <text x="26" y="38" text-anchor="middle" font-family="Exo 2, sans-serif" font-weight="600" font-size="32" fill="#1579c4">P</text>
            </svg>
          </div>
          <p class="step-text">Every time a motorist books one of your spaces, you'll receive a booking alert via text &amp; email, there are no phone calls involved and you don't need to meet the motorists as they will display a booking slip in their car windscreen so you will know the space has been booked and paid for.</p>
        </div>

        <div class="step step-three">
          <div class="step-badge">Earn money<br>from your<br>space
            <svg class="step-icon" style="top:88px" width="52" height="52" viewBox="0 0 52 52">
              <circle cx="26" cy="26" r="23" fill="none" stroke="#fff" stroke-width="3"/>
              <text x="26" y="38" text-anchor="middle" font-family="Exo 2, sans-serif" font-weight="600" font-size="32" fill="#fff">£</text>
            </svg>
          </div>
          <p class="step-text">We will collect the fees securely online for you and you can withdraw funds for every day your space(s) have been used.</p>
        </div>
      </section>

      <p class="eligibility-note">Please note we only accept adverts from businesses &amp; organisations.</p>
    </main>
  </div>
</body>
</html>
```